Pediatric Dentist Business Card

I need a business card designed for a dentist who works exclusively with children.
We prefer designs that are out of ordiary that is fun and interesting to kids.

there is no logo since this is a dentists office. The name of the doctor is "Tavro Kine" if you want to get creative with that.

Target Market(s)

Kids

Industry/Entity Type

Business

Contact Information for Business Card

Anythings that is creative

Colors

Designer to choose colors to be used in the design.

```html
<!DOCTYPE html>
<html lang="en">
<head>
<meta charset="utf-8">
<title>Tavro Kine – Pediatric Dentist Business Card</title>
<link rel="stylesheet" href="https://fonts.googleapis.com/css2?family=Montserrat:wght@400;500;700&display=swap">
<style>
  :root {
    --backdrop: #3a2a22;
    --teal: #14b09f;
    --teal-back: #17a597;
    --yellow: #fcd96e;
    --name-yellow: #fbd257;
    --white: #ffffff;
    --ink: #5a5650;
    --icon-blue: #1f6fc0;
    --icon-orange: #ee6b2e;
    --icon-pink: #f08bb5;
    --icon-green: #5bb64a;
  }
  * { margin: 0; padding: 0; box-sizing: border-box; }
  html, body { width: 1200px; height: 1000px; overflow: hidden; }
  body {
    background: var(--backdrop);
    font-family: "Montserrat", Arial, sans-serif;
    position: relative;
  }
  .card {
    position: absolute;
    width: 520px;
    height: 295px;
    border-radius: 24px;
    overflow: hidden;
  }
  .card-front { left: 140px; top: 150px; background: var(--white); }
  .card-back { left: 540px; top: 540px; background: var(--teal-back); }

  .front-shapes { position: absolute; inset: 0; }

  .identity { position: absolute; left: 38px; top: 122px; color: var(--white); }
  .identity-name { font-size: 27px; font-weight: 700; line-height: 1.1; }
  .identity-name .surname { color: var(--name-yellow); }
  .identity-role { font-size: 18px; font-weight: 400; margin-top: 2px; }

  .contacts { position: absolute; left: 218px; top: 42px; list-style: none; }
  .contact { display: flex; align-items: center; height: 56px; }
  .contact-icon {
    width: 36px; height: 36px; border-radius: 50%;
    display: flex; align-items: center; justify-content: center;
    flex: none; margin-right: 16px;
  }
  .contact-icon svg { width: 18px; height: 18px; }
  .icon-phone { background: var(--icon-blue); }
  .icon-web { background: var(--icon-orange); }
  .icon-mail { background: var(--icon-pink); }
  .icon-pin { background: var(--icon-green); }
  .contact-text { font-size: 14px; font-weight: 500; color: var(--ink); line-height: 1.2; }

  .back-content {
    position: absolute; inset: 0;
    display: flex; flex-direction: column; align-items: center; justify-content: center;
    color: var(--white); text-align: center;
  }
  .back-mark { width: 70px; height: 70px; border-radius: 50%; background: var(--white); margin-bottom: 24px; }
  .back-name { font-size: 27px; font-weight: 700; line-height: 1.1; }
  .back-role { font-size: 18px; font-weight: 400; margin-top: 4px; }
</style>
</head>
<body>

<section class="card card-front">
  <svg class="front-shapes" viewBox="0 0 520 295" width="520" height="295" aria-hidden="true">
    <path d="M190 0 H520 V295 H255 C300 200 285 80 190 0 Z" fill="var(--yellow)"/>
    <path d="M0 0 H172 C250 70 255 215 70 278 L0 292 Z" fill="var(--teal)"/>
  </svg>

  <div class="identity">
    <div class="identity-name">Tavro <span class="surname">Kine</span></div>
    <div class="identity-role">Pediatric Dentist</div>
  </div>

  <ul class="contacts">
    <li class="contact">
      <span class="contact-icon icon-phone">
        <svg viewBox="0 0 24 24"><path fill="#fff" d="M6.6 10.8a15 15 0 0 0 6.6 6.6l2.2-2.2a1 1 0 0 1 1-.25 11.4 11.4 0 0 0 3.6.57 1 1 0 0 1 1 1V20a1 1 0 0 1-1 1A17 17 0 0 1 3 4a1 1 0 0 1 1-1h3.5a1 1 0 0 1 1 1c0 1.25.2 2.45.57 3.6a1 1 0 0 1-.25 1z"/></svg>
      </span>
      <span class="contact-text">123 456 789</span>
    </li>
    <li class="contact">
      <span class="contact-icon icon-web">
        <svg viewBox="0 0 24 24" fill="none" stroke="#fff" stroke-width="2"><circle cx="12" cy="12" r="9"/><path d="M3 12h18M12 3c3 3 3 15 0 18M12 3c-3 3-3 15 0 18"/></svg>
      </span>
      <span class="contact-text">www.youesitegoeshere.com</span>
    </li>
    <li class="contact">
      <span class="contact-icon icon-mail">
        <svg viewBox="0 0 24 24"><rect x="3" y="6" width="18" height="12" rx="1" fill="#fff"/><path d="M3 7l9 6 9-6" fill="none" stroke="var(--icon-pink)" stroke-width="1.5"/></svg>
      </span>
      <span class="contact-text">email@domaingoeshere.com</span>
    </li>
    <li class="contact">
      <span class="contact-icon icon-pin">
        <svg viewBox="0 0 24 24"><path fill="#fff" d="M12 2a7 7 0 0 0-7 7c0 5 7 13 7 13s7-8 7-13a7 7 0 0 0-7-7zm0 9.5A2.5 2.5 0 1 1 12 6.5a2.5 2.5 0 0 1 0 5z"/></svg>
      </span>
      <span class="contact-text">Street Name, Zip Code<br>1234, City</span>
    </li>
  </ul>
</section>

<section class="card card-back">
  <div class="back-content">
    <div class="back-mark"></div>
    <div class="back-name">Tavro Kine</div>
    <div class="back-role">Pediatric Dentist</div>
  </div>
</section>

</body>
</html>
```